Business Card Design

I am a florist specialising in weddings. I would like a very modern however elegant and simple design. My arrangement designs can be quite rustic with a vintage feel, so if you are able to reflect this in the card that would be great.
Updates

Thank you everyone for your submissions. I have found some further words for inspiration. I am looking for something more earthy and artisan looking. If possible I would like to use 100% recycled paper - the type that even looks rustic and recycled. I may even opt to use a small logo to emphasis the fact that they are made from recycled paper. I know this is quite different to my original brief but I wasn't quite sure what to expect from your designs. Also, with the logo, I give permission for it to be cropped to remove the 'Floral Designer' text. Please contact me if you need any further assistance. Many thanks Lisette Petal and Thistle Studio

I would prefer not to have any photgraphs & not too much pink. Thank you!

Industry/Entity Type

Florist

Contact Information for Business Card

Lisette Varko
Floral Designer
0417 365 820
lisette@petalthistlestudio.com.au
petalthistlestudio.com.au

Requirements
Must have
• My logo

```html
<!DOCTYPE html>
<html lang="en">
<head>
<meta charset="utf-8">
<title>Petal and Thistle Studio – Business Card</title>
<link href="https://fonts.googleapis.com/css2?family=Tenor+Sans&display=swap" rel="stylesheet">
<style>
  :root {
    --stage: #d9d9d9;
    --paper: #fbf8f2;
    --ink: #1c1c1c;
    --plum: #8c2d5c;
    --oak: #9a7a62;
    --linen: #d8c6b0;
    --sage: #a9ae96;
    --iron: #4a4540;
    --card-shadow: rgba(0, 0, 0, 0.28);
  }
  * { box-sizing: border-box; margin: 0; padding: 0; }
  html, body {
    width: 1200px;
    height: 1000px;
    overflow: hidden;
    background: var(--stage);
    font-family: "Tenor Sans", "Trebuchet MS", sans-serif;
  }
  .canvas {
    position: relative;
    width: 1200px;
    height: 1000px;
  }
  .card {
    position: absolute;
    box-shadow: 0 6px 14px var(--card-shadow);
  }
  /* Front side: muted earthy field where the arrangement image sits */
  .card-front {
    left: 60px;
    top: 170px;
    width: 440px;
    height: 660px;
    background: linear-gradient(170deg, var(--oak) 0%, var(--linen) 40%, var(--sage) 72%, var(--iron) 100%);
  }
  /* Back side: contact details and studio name */
  .card-back {
    left: 540px;
    top: 311px;
    width: 620px;
    height: 378px;
    background: var(--paper);
    color: var(--ink);
  }
  .holder-name {
    position: absolute;
    left: 40px;
    top: 30px;
    font-size: 24px;
    font-weight: 400;
    color: var(--plum);
    letter-spacing: 0.3px;
  }
  .holder-role {
    position: absolute;
    left: 40px;
    top: 62px;
    font-size: 17px;
  }
  .contact-list {
    position: absolute;
    left: 40px;
    top: 130px;
    list-style: none;
    font-size: 15px;
    line-height: 22px;
  }
  .studio-mark {
    position: absolute;
    right: 30px;
    top: 196px;
    text-align: right;
  }
  .studio-name {
    font-size: 22px;
    display: flex;
    align-items: center;
    gap: 8px;
    justify-content: flex-end;
  }
  .studio-dot {
    width: 12px;
    height: 12px;
    border-radius: 50%;
    background: var(--plum);
  }
  .studio-tagline {
    margin-top: 4px;
    margin-right: 60px;
    font-size: 15px;
  }
  .abn {
    position: absolute;
    right: 34px;
    bottom: 28px;
    font-size: 16px;
    letter-spacing: 0.5px;
  }
</style>
</head>
<body>
  <main class="canvas">
    <div class="card card-front" role="img" aria-label="Image area for a rustic wedding bouquet resting on a wooden bench"></div>

    <section class="card card-back">
      <h1 class="holder-name">Lisette Varko</h1>
      <p class="holder-role">Floral Designer</p>
      <ul class="contact-list">
        <li>0417 365 820</li>
        <li>lisette@petalthistlestudio.com.au</li>
        <li>www.petalthistlestudio.com.au</li>
      </ul>
      <div class="studio-mark">
        <p class="studio-name"><span>Petal and Thistle Studio</span><span class="studio-dot"></span></p>
        <p class="studio-tagline">Floral Designer</p>
      </div>
      <p class="abn">ABN: 71 204 583 619</p>
    </section>
  </main>
</body>
</html>
```